Simple Business Cards for Self-employed Coach

Simple business card with a design that includes the QLT logo.
Using either only the logo color or additional colors that match the logo.

Meridian Guides reach deeply into the past, gathering wisdom from East and West, while still staying current with the frontiers of new discovery in cognitive science, genetics, and other disciplines. see https://www.brightharborpath.example/what-is-integral-coaching/

Target Market(s)

Coaching Clients in Tokyo /Asia; in business organizations, but also outside

Industry/Entity Type

Life Coaching

Contact Information for Business Card

Lukas Brenning
Certified Meridian Guide

3-2-48 Kamiyoshi
Nakarino 164-0392
Tokyo, Japan

Phone: +81 70 4817 5062
E-Mail: lukas.brenning@mailora.example

Font styles to use
Sans Serif

Colors
00a990

Requirements
Must have
• include uploaded logo
• color fitting with QLT logo color
Nice to have
• simple, elegant design
Should not have
• clutter

```html
<!DOCTYPE html>
<html lang="en">
<head>
<meta charset="utf-8">
<title>Lukas Brenning – Business Card</title>
<link rel="stylesheet" href="https://fonts.googleapis.com/css2?family=Antonio:wght@400;500;600&display=swap">
<style>
  :root {
    --teal-deep: #17695f;
    --teal-mid: #5f9a8e;
    --paper: #e7ded1;
    --ink: #0e3a35;
    --brand: #0f6257;
    --contact: #dcc8aa;
  }
  html, body {
    margin: 0;
    padding: 0;
    width: 1200px;
    height: 660px;
    overflow: hidden;
  }
  .card {
    position: relative;
    width: 1200px;
    height: 660px;
    overflow: hidden;
    background: linear-gradient(100deg, var(--teal-deep) 0%, var(--teal-mid) 38%, #b9c8bc 62%, var(--paper) 85%);
    font-family: "Antonio", "Arial Narrow", sans-serif;
  }
  .contact {
    position: absolute;
    left: 53px;
    top: 56px;
    margin: 0;
    color: var(--contact);
    font-size: 38px;
    font-weight: 400;
    line-height: 62px;
    letter-spacing: 0.3px;
  }
  .contact p { margin: 0; }
  .brand {
    position: absolute;
    left: 724px;
    top: 52px;
    display: flex;
    align-items: center;
    gap: 22px;
  }
  .brand-square {
    width: 60px;
    height: 60px;
    background: var(--brand);
  }
  .brand-name {
    color: var(--brand);
    font-size: 92px;
    font-weight: 600;
    line-height: 1;
    letter-spacing: 6px;
  }
  .identity {
    position: absolute;
    left: 0;
    right: 0;
    top: 300px;
    text-align: center;
    color: var(--ink);
  }
  .name {
    margin: 0;
    font-size: 66px;
    font-weight: 500;
    line-height: 1;
    letter-spacing: 0.5px;
  }
  .title {
    margin: 30px 0 0;
    font-size: 52px;
    font-weight: 500;
    line-height: 1;
    letter-spacing: 0.5px;
  }
  .address {
    position: absolute;
    left: 0;
    right: 0;
    top: 586px;
    margin: 0;
    text-align: center;
    color: var(--ink);
    font-size: 40px;
    font-weight: 400;
    line-height: 1;
    letter-spacing: 0.3px;
  }
</style>
</head>
<body>
  <main class="card">
    <div class="contact">
      <p class="contact-phone">t: +81 70 4817 5062</p>
      <p class="contact-email">e: lukas.brenning@mailora.example</p>
    </div>

    <div class="brand">
      <span class="brand-square"></span>
      <span class="brand-name">QLT</span>
    </div>

    <section class="identity">
      <h1 class="name">Lukas Brenning</h1>
      <p class="title">Certified Meridian Guide</p>
    </section>

    <p class="address">3-2-48 Kamiyoshi, Nakarino 164-0392, Tokyo, Japan</p>
  </main>
</body>
</html>
```